Whitmore Business Card Design

The name of the business is Dara Whitmore, CPA LLC
The service that we offer is Accounting, Tax & Consulting Services. I need it to have the following items:
Dara Whitmore, Principal
Phone Number
Email Address
Physical Address

I have attached the company logo, one in black and one in white. Please provide a design in black background and the other in white background. Please include "Accounting, Tax & Consulting Services". I want the business card to be clean and very professional.

```html
<!DOCTYPE html>
<html lang="en">
<head>
<meta charset="utf-8">
<title>Dara Whitmore, CPA LLC – Business Cards</title>
<link rel="stylesheet" href="https://fonts.googleapis.com/css2?family=Montserrat:wght@400;500;600;700;800&display=swap">
<style>
  :root {
    --backdrop: #1c1c1c;
    --card-dark: #222223;
    --card-light: #ffffff;
    --brand-red: #9b1b1f;
    --brand-grey: #6e6e70;
    --text-dark: #1e1e1e;
    --text-light: #e8e8e8;
  }
  * { box-sizing: border-box; margin: 0; padding: 0; }
  html, body {
    width: 1200px; height: 927px; overflow: hidden;
    background: var(--backdrop);
    font-family: "Montserrat", sans-serif;
  }
  .stage {
    width: 1200px; height: 927px;
    display: flex; flex-direction: column; align-items: center; justify-content: center;
    gap: 40px;
  }
  .card {
    width: 720px; height: 412px; border-radius: 26px; position: relative; overflow: hidden;
    box-shadow: 0 14px 30px rgba(0,0,0,.45);
  }

  /* Front (dark) */
  .card--front { background: var(--card-dark); display: flex; align-items: center; justify-content: center; }
  .front-lockup { display: flex; align-items: center; gap: 22px; }
  .brand-square { width: 58px; height: 58px; background: var(--brand-red); flex-shrink: 0; }
  .front-lockup .brand-name { font-size: 34px; font-weight: 500; color: var(--brand-grey); letter-spacing: 1px; line-height: 1; }
  .front-lockup .brand-title { font-size: 21px; font-weight: 600; color: #8a8a8c; letter-spacing: 3.5px; margin-top: 10px; }
  .front-lockup .brand-services { font-size: 17px; font-weight: 700; color: #7c7c7e; margin-top: 12px; letter-spacing: .3px; }

  /* Back (light) */
  .card--back { background: var(--card-light); }
  .back-brand { position: absolute; left: 62px; top: 52px; display: flex; align-items: center; gap: 14px; }
  .back-brand .brand-square { width: 40px; height: 40px; }
  .back-brand .brand-name { font-size: 21px; font-weight: 600; color: var(--text-dark); line-height: 1; }
  .back-brand .brand-title { font-size: 11px; font-weight: 500; color: #8a8a8a; letter-spacing: 2px; margin-top: 6px; }

  .person { position: absolute; left: 62px; top: 150px; font-size: 25px; font-weight: 800; color: var(--brand-red); letter-spacing: .3px; }
  .divider { position: absolute; left: 62px; right: 40px; top: 196px; height: 2px; background: var(--brand-red); }

  .contacts { position: absolute; left: 0; top: 226px; list-style: none; }
  .contacts li { display: flex; align-items: center; gap: 18px; height: 44px; margin-bottom: 6px; }
  .contact-tab {
    width: 74px; height: 40px; background: var(--brand-red);
    border-radius: 0 10px 10px 0; display: flex; align-items: center; justify-content: flex-end; padding-right: 16px;
  }
  .contact-tab svg { width: 20px; height: 20px; }
  .contacts span { font-size: 18px; font-weight: 500; color: var(--text-dark); }

  .address { position: absolute; right: 44px; top: 246px; text-align: right; font-size: 17px; font-weight: 500; color: var(--text-dark); line-height: 1.6; }
</style>
</head>
<body>
<main class="stage">

  <section class="card card--front" aria-label="Card front">
    <div class="front-lockup">
      <div class="brand-square"></div>
      <div>
        <div class="brand-name">Dara Whitmore, CPA LLC</div>
        <div class="brand-title">CERTIFIED PUBLIC ACCOUNTANT</div>
        <div class="brand-services">Accounting, Tax &amp; Consulting Services</div>
      </div>
    </div>
  </section>

  <section class="card card--back" aria-label="Card back">
    <div class="back-brand">
      <div class="brand-square"></div>
      <div>
        <div class="brand-name">Dara Whitmore, CPA LLC</div>
        <div class="brand-title">CERTIFIED PUBLIC ACCOUNTANT</div>
      </div>
    </div>

    <h1 class="person">DARA WHITMORE, PRINCIPAL</h1>
    <div class="divider"></div>

    <ul class="contacts">
      <li>
        <div class="contact-tab">
          <svg viewBox="0 0 24 24" fill="#fff"><path d="M6.6 10.8a15.1 15.1 0 0 0 6.6 6.6l2.2-2.2a1 1 0 0 1 1-.25 11.4 11.4 0 0 0 3.6.57 1 1 0 0 1 1 1V20a1 1 0 0 1-1 1A17 17 0 0 1 3 4a1 1 0 0 1 1-1h3.5a1 1 0 0 1 1 1c0 1.25.2 2.45.57 3.57a1 1 0 0 1-.25 1z"/></svg>
        </div>
        <span>555-014-2236</span>
      </li>
      <li>
        <div class="contact-tab">
          <svg viewBox="0 0 24 24" fill="none" stroke="#fff" stroke-width="2"><rect x="3" y="5" width="18" height="14" rx="1"/><path d="M3 6l9 7 9-7"/></svg>
        </div>
        <span>info@darawhitmorecpa.com</span>
      </li>
      <li>
        <div class="contact-tab">
          <svg viewBox="0 0 24 24" fill="none" stroke="#fff" stroke-width="2"><circle cx="12" cy="12" r="9"/><path d="M3 12h18M12 3c3 3.5 3 14.5 0 18M12 3c-3 3.5-3 14.5 0 18"/></svg>
        </div>
        <span>www.darawhitmorecpa.com</span>
      </li>
    </ul>

    <address class="address" style="font-style:normal">
      Harbor Point 2100 Oak Ridge<br>
      Ave Suite 310
    </address>
  </section>

</main>
</body>
</html>
```